Visitenkarten-Design für Erfindung & Entwicklung von Produkten für Körper, Geist und Seele
Zielgruppe
Erfindung und Entwicklung von Produkten für Körper Geist und Seele
Als grosser Überbegriff Produkte zur Regenration und Wohlbefinden sowie Bewusstseins Förderung
' Beispiel ' www. o-senva.ch
Zielgruppe Jedermann und Jedefrau die Ihr Bewusstein für Ihre Gesundheit und Heilung auf allen Ebenen vertiefen möchte ....
Aufgabenstellung
Das Logo ist Entwickelt in einem Entwurfsstadium kleine Verbesserungsvorschläge wären möglich
Vorallem geht es um das Layout und der sauberen Daten Erfassung
sowie die Gestaltung der Visitenkarte

```html
<!DOCTYPE html>
<html lang="de">
<head>
<meta charset="utf-8">
<title>Velunar Visitenkarte</title>
<link href="https://fonts.googleapis.com/css2?family=Montserrat:wght@300;400;600&display=swap" rel="stylesheet">
<style>
  :root {
    --backdrop: #cfcfcf;
    --card: #f7f7f7;
    --band: #62861e;
    --ink: #2b2b2b;
    --muted: #555555;
    --accent: #d9862a;
    --gold: #b68a2e;
  }
  html, body {
    margin: 0;
    width: 1200px;
    height: 906px;
    overflow: hidden;
    background: var(--backdrop);
    font-family: "Montserrat", sans-serif;
  }
  .sheet {
    position: relative;
    width: 1200px;
    height: 906px;
    display: flex;
    justify-content: center;
    align-items: center;
    gap: 40px;
  }
  .card {
    position: relative;
    width: 540px;
    height: 350px;
    background: var(--card);
    box-shadow: 0 2px 6px rgba(0,0,0,0.12);
    overflow: hidden;
  }
  /* Front */
  .card__band {
    position: absolute;
    top: 0; left: 0; right: 0;
    height: 104px;
    background: var(--band);
  }
  .address {
    position: absolute;
    top: 18px; left: 28px;
    color: #ffffff;
    font-size: 14px;
    line-height: 21px;
    letter-spacing: 1.6px;
    font-weight: 400;
  }
  .address__company { font-weight: 600; }
  .brand {
    position: absolute;
    top: 132px; left: 28px;
  }
  .brand__name {
    font-size: 30px;
    font-weight: 300;
    letter-spacing: 7px;
    color: var(--muted);
  }
  .brand__tagline {
    margin-top: 6px;
    margin-left: 60px;
    font-size: 13px;
    font-weight: 400;
    letter-spacing: 1px;
    color: var(--gold);
  }
  .contact {
    position: absolute;
    right: 30px; bottom: 28px;
    text-align: right;
    color: var(--ink);
    font-size: 13px;
    letter-spacing: 1.4px;
    line-height: 22px;
  }
  .contact__name {
    font-size: 15px;
    font-weight: 600;
    letter-spacing: 4px;
  }
  .contact__first { color: var(--accent); }
  /* Back */
  .back__name {
    position: absolute;
    top: 50%; left: 50%;
    transform: translate(-50%, -60%);
    font-size: 44px;
    font-weight: 300;
    letter-spacing: 12px;
    color: var(--band);
  }
  .back__web {
    position: absolute;
    right: 30px; bottom: 26px;
    font-size: 13px;
    letter-spacing: 3px;
    color: var(--ink);
  }
</style>
</head>
<body>
  <main class="sheet">
    <section class="card card--front">
      <div class="card__band"></div>
      <div class="address">
        <div class="address__company">Velunar</div>
        <div>Lindenweg 14</div>
        <div>8400 TALBACH</div>
      </div>
      <div class="brand">
        <div class="brand__name">Velunar</div>
        <div class="brand__tagline">neues schaffen</div>
      </div>
      <div class="contact">
        <div class="contact__name"><span class="contact__first">LIRA</span> SANTEN</div>
        <div>kolutrisvend@velunar.ch</div>
        <div>T. 079 614 27 83</div>
      </div>
    </section>
    <section class="card card--back">
      <div class="back__name">Velunar</div>
      <div class="back__web">www. velunar.ch</div>
    </section>
  </main>
</body>
</html>
```